flat share room mate rental website(design only)

We need a design for the homepage of a flat share / roommate website. We have a website template http://demo1.hometemplix.net and we're looking for a homepage similar to this http://uk.bunkpalora.com but different.
The main user of the site are likely to be students and young professionals so were not looking for anything too serious.
We want to emphasise that the website will be 100% free to use both to post an advert and to contact the advertiser.
We must have a 'new rooms' and new flatmates carousel, also we would prefer if the menu had only a login button and maybe a 'post a room' button.
Our logo is currently being designed, so you can put anything in its place.
We look forward to seeing what you guys come up with.
Target Market(s)
Students, Young Professionals
Industry/Entity Type
Rental
Number of Pages Required
1 page
Look and feel
Each slider illustrates characteristics of the customer's brand and the style your logo design should communicate.

```html
<!DOCTYPE html>
<html lang="en">
<head>
<meta charset="utf-8">
<title>Flat Share – Share the Room</title>
<link rel="stylesheet" href="https://fonts.googleapis.com/css2?family=Arimo:wght@400;700&family=Tinos:wght@400;700&display=swap">
<style>
:root{
  --cyan:#8ad9e6;
  --cyan-deep:#3fb6cc;
  --cyan-soft:#e3f7fa;
  --btn:#b9ecd9;
  --btn-edge:#3d9b86;
  --ink:#1d1d1d;
  --muted:#555;
  --peach:#fbe6d6;
  --orange:#ea8c22;
  --footer:#5b5b5b;
  --white:#ffffff;
}
*{box-sizing:border-box;margin:0;padding:0}
html,body{width:1200px;height:3924px;overflow:hidden;background:var(--white)}
body{position:relative;font-family:"Arimo",Arial,sans-serif;color:var(--ink)}
.abs{position:absolute}

/* header */
.site-header{position:absolute;left:0;top:0;width:1200px;height:98px;background:var(--white)}
.logo{left:82px;top:8px;font-family:"Tinos",serif;font-size:40px;color:var(--cyan-deep)}
.main-nav{left:88px;top:60px;display:flex;gap:50px;font-family:"Tinos",serif;font-weight:700;font-size:15px}
.login{left:940px;top:48px;font-size:16px;color:var(--cyan-deep)}
.lang-flag{left:1070px;top:38px;width:28px;height:20px;background:#d21f1f}

/* hero */
.hero{left:0;top:98px;width:1200px;height:605px;background:linear-gradient(180deg,#c9dfe6 0%,#d7a98e 45%,#a86f5b 75%,#7d8ea6 100%)}
.hero-btn{top:75px;font-size:21px;color:var(--white);text-shadow:0 1px 3px rgba(0,0,0,.5)}
.hero-title{left:0;width:1200px;text-align:center;color:var(--white);font-weight:700;font-size:56px;letter-spacing:1px;text-shadow:0 2px 6px rgba(0,0,0,.35)}
.hero-rule{left:90px;top:380px;width:1040px;height:4px;background:var(--white)}

/* free band */
.free-band{left:0;top:703px;width:1200px;height:294px;background:linear-gradient(180deg,#f4fcfd,#d6f2f6)}
.free-lead{left:104px;top:64px;font-size:46px;color:var(--cyan)}
.free-line{left:104px;font-size:31px;color:var(--cyan)}
.cta-box{left:1046px;width:98px;height:84px;background:var(--btn);border:3px solid var(--btn-edge);display:flex;align-items:center;justify-content:center;text-align:center;font-weight:700;font-size:17px;line-height:1.3}

/* flatmate photo */
.flatmate-photo{left:0;top:997px;width:1200px;height:442px;background:linear-gradient(180deg,#c9d7de 0%,#d8dde0 40%,#e9e6e2 55%,#b59d84 100%)}
.flatmate-bar{left:0;top:1292px;width:1200px;height:75px;background:rgba(40,40,40,.45);text-align:center;line-height:75px;color:var(--white);font-size:46px;letter-spacing:7px}

/* testimonials */
.big-title{left:0;top:1458px;width:1200px;text-align:center;font-weight:700;font-size:66px;color:var(--cyan);letter-spacing:2px}
.avatar{width:104px;height:104px;border-radius:50%;background:radial-gradient(circle at 50% 45%,#d9b39a,#8a6a58);border:3px solid var(--white);box-shadow:0 0 0 1px #ccc}
.quote{font-family:"Tinos",serif;font-size:15px;line-height:1.15;color:var(--cyan-deep);text-align:center;width:150px}

/* listings */
.section-title{left:0;width:1200px;text-align:center;font-weight:700;font-size:28px}
.section-rule{left:445px;width:310px;height:4px;background:var(--ink)}
.card{width:278px;height:314px;background:var(--peach)}
.card-photo{position:absolute;left:12px;top:12px;width:254px;height:168px}
.card-text{position:absolute;left:16px;top:205px;width:246px;text-align:center;font-family:"Tinos",serif;font-size:13px;line-height:1.45;color:var(--cyan-deep)}
.slider-arrow{width:36px;height:40px;background:var(--orange);border-radius:5px}

/* ambition band */
.ambition{left:0;top:2838px;width:1200px;height:383px;background:linear-gradient(180deg,#c94a3b 0%,#7fa3c9 45%,#2f6fb2 100%)}
.ambition-text{left:0;width:1200px;text-align:center;color:var(--white);font-weight:700;font-size:47px;text-shadow:0 2px 4px rgba(0,0,0,.35)}

/* agents */
.agent{width:86px;height:86px;border-radius:50%;background:radial-gradient(circle at 50% 45%,#d4ad94,#6d5446);border:3px solid var(--white);box-shadow:0 0 0 1px #bbb}
.agent-note{font-family:"Tinos",serif;font-size:12px;line-height:1.3;color:var(--cyan-deep);width:118px;text-align:center}
.to-top{left:1110px;top:3470px;width:44px;height:44px;background:#d2f1f3}

/* footer */
.footer-map{left:0;top:3532px;width:1200px;height:353px;background:linear-gradient(160deg,#d7a24e 0%,#c98b3c 50%,#b57a36 100%)}
.footer-head{font-family:"Tinos",serif;font-weight:700;font-size:22px;color:var(--white)}
.footer-head::after{content:"";display:block;width:100%;height:3px;background:var(--white);margin-top:4px}
.city-list{left:157px;top:3660px;list-style:none;font-family:"Tinos",serif;font-weight:700;font-size:14px;line-height:23px;color:var(--ink)}
.field{height:24px;background:#dfe9ec;border-radius:3px;font-size:11px;color:var(--muted);line-height:24px;padding-left:10px}
.search-btn{left:790px;top:3718px;width:28px;height:26px;background:var(--cyan-deep);border-radius:3px}
.social-icon{width:28px;height:28px;border-radius:4px}
.legal-bar{left:0;top:3885px;width:1200px;height:39px;background:var(--footer);color:#e8e8e8;font-size:11px;line-height:39px}
</style>
</head>
<body>

<header class="site-header">
  <div class="abs logo">LOGO</div>
  <nav class="abs main-nav"><span>HOME</span><span>PROPERTIES</span><span>BLOG</span><span>AGENTS</span><span>CONTACT US</span></nav>
  <div class="abs login">Login</div>
  <div class="abs lang-flag" role="img" aria-label="Language selector"></div>
</header>

<section class="abs hero" role="img" aria-label="Photo of smiling young friends together">
  <div class="abs hero-btn" style="left:770px">Post Room</div>
  <div class="abs hero-btn" style="left:962px">Search Room</div>
  <h1 class="abs hero-title" style="top:300px">SHARE THE ROOM</h1>
  <div class="abs hero-rule"></div>
  <div class="abs hero-title" style="top:385px">SHARE THE HAPPINESS</div>
</section>

<section class="abs free-band">
  <p class="abs free-lead">No fees. We don’t charge you anything.</p>
  <p class="abs free-line" style="top:140px">No fees to post an advert</p>
  <p class="abs free-line" style="top:180px">No fees to contact your potential new flatmate.</p>
  <div class="abs cta-box" style="top:65px">RENT<br>A<br>ROOM</div>
  <div class="abs cta-box" style="top:206px">POST<br>A<br>ROOM</div>
</section>

<section class="abs flatmate-photo" role="img" aria-label="Photo of friends sitting arm in arm on a beach">
</section>
<div class="abs flatmate-bar">Find your Perfect Flatmate</div>

<h2 class="abs big-title">GIVE THE BEST GET THE BEST</h2>

<div class="abs avatar" style="left:144px;top:1568px" role="img" aria-label="Customer portrait"></div>
<p class="abs quote" style="left:275px;top:1588px">Amazing company!<br>I found a roommate<br>in 2 days<br>without hassle<br>Thanks for your help</p>
<div class="abs avatar" style="left:652px;top:1568px" role="img" aria-label="Customer portrait"></div>
<p class="abs quote" style="left:783px;top:1588px">Amazing company!<br>I found a roommate<br>in 2 days<br>without hassle<br>Thanks for your help</p>
<div class="abs avatar" style="left:144px;top:1730px" role="img" aria-label="Customer portrait"></div>
<p class="abs quote" style="left:275px;top:1750px">Amazing company!<br>I found a roommate<br>in 2 days<br>without hassle<br>Thanks for your help</p>
<div class="abs avatar" style="left:652px;top:1730px" role="img" aria-label="Customer portrait"></div>
<p class="abs quote" style="left:783px;top:1750px">Amazing company!<br>I found a roommate<br>in 2 days<br>without hassle<br>Thanks for your help</p>

<h2 class="abs section-title" style="top:1896px">FIND THE FLATS</h2>
<div class="abs section-rule" style="top:1938px"></div>

<article class="abs card" style="left:88px;top:2001px">
  <div class="card-photo" role="img" aria-label="Photo of a villa with pool by the sea" style="background:linear-gradient(180deg,#6fb3e2,#e8eef0 60%,#3b9bc5)"></div>
  <p class="card-text">2 Bedrooms | 2 Baths | Sea View<br>Fully furnished, bills included, close to campus.</p>
</article>
<article class="abs card" style="left:458px;top:2001px">
  <div class="card-photo" role="img" aria-label="Photo of a modern house with lawn" style="background:linear-gradient(180deg,#dfe6ea,#9aa7a3 50%,#4f8f3a)"></div>
  <p class="card-text">Modern villa with garden and bright shared lounge, five minutes from the station.</p>
</article>
<article class="abs card" style="left:824px;top:2001px">
  <div class="card-photo" role="img" aria-label="Photo of a lit house with pool at dusk" style="background:linear-gradient(180deg,#2b3d63,#c1793b 55%,#2f6f8a)"></div>
  <p class="card-text">Poolside house with spacious rooms and friendly flatmates, ideal for young professionals.</p>
</article>
<div class="abs slider-arrow" style="left:87px;top:2328px"><svg width="36" height="40" viewBox="0 0 36 40"><path d="M22 10 L12 20 L22 30" fill="none" stroke="#fff" stroke-width="5"/></svg></div>
<div class="abs slider-arrow" style="left:1065px;top:2328px"><svg width="36" height="40" viewBox="0 0 36 40"><path d="M14 10 L24 20 L14 30" fill="none" stroke="#fff" stroke-width="5"/></svg></div>

<h2 class="abs section-title" style="top:2354px">FIND THE ROOM</h2>
<div class="abs section-rule" style="top:2396px"></div>

<article class="abs card" style="left:88px;top:2459px">
  <div class="card-photo" role="img" aria-label="Photo of a warm lit bedroom" style="background:linear-gradient(180deg,#3a2618,#a9744a 55%,#5a3a22)"></div>
  <p class="card-text">Cosy double room with desk and wardrobe, quiet street near the city centre.</p>
</article>
<article class="abs card" style="left:458px;top:2459px">
  <div class="card-photo" role="img" aria-label="Photo of a bright twin bedroom" style="background:linear-gradient(180deg,#d9d3c8,#b9a58c 55%,#8a6b52)"></div>
  <p class="card-text">Bright twin room in a shared flat, all bills and fast internet included.</p>
</article>
<article class="abs card" style="left:824px;top:2459px">
  <div class="card-photo" role="img" aria-label="Photo of a bedroom with lake view" style="background:linear-gradient(180deg,#8fb2c4,#c9b79d 55%,#6e5a46)"></div>
  <p class="card-text">Ensuite room with lake view, shared kitchen and weekly cleaning included.</p>
</article>
<div class="abs slider-arrow" style="left:87px;top:2780px"><svg width="36" height="40" viewBox="0 0 36 40"><path d="M22 10 L12 20 L22 30" fill="none" stroke="#fff" stroke-width="5"/></svg></div>
<div class="abs slider-arrow" style="left:1065px;top:2780px"><svg width="36" height="40" viewBox="0 0 36 40"><path d="M14 10 L24 20 L14 30" fill="none" stroke="#fff" stroke-width="5"/></svg></div>

<section class="abs ambition" role="img" aria-label="Photo of friends in ski wear forming a circle under a blue sky">
  <p class="abs ambition-text" style="top:140px">YOUR SATISFACTION IS OUR AMBITION</p>
  <p class="abs ambition-text" style="top:205px">FIND THE PERFECT PARTNER</p>
</section>

<h2 class="abs section-title" style="top:3270px;font-size:22px;font-family:'Tinos',serif">THROUGH THE AGENT</h2>
<div class="abs section-rule" style="top:3304px;left:432px;width:336px"></div>

<div class="abs agent" style="left:186px;top:3384px" role="img" aria-label="Agent portrait"></div>
<p class="abs agent-note" style="left:278px;top:3385px">Friendly agent, happy<br>to help you settle in.</p>
<div class="abs agent" style="left:398px;top:3384px" role="img" aria-label="Agent portrait"></div>
<p class="abs agent-note" style="left:490px;top:3385px">Local expert, always<br>ready to show rooms.</p>
<div class="abs agent" style="left:650px;top:3384px" role="img" aria-label="Agent portrait"></div>
<p class="abs agent-note" style="left:760px;top:3385px">Quick replies, honest<br>advice for new tenants.</p>
<div class="abs agent" style="left:895px;top:3384px" role="img" aria-label="Agent portrait"></div>
<div class="abs to-top"><svg width="44" height="44" viewBox="0 0 44 44"><path d="M12 27 L22 17 L32 27" fill="none" stroke="#3fb6cc" stroke-width="4"/></svg></div>

<footer>
  <div class="abs footer-map" role="img" aria-label="World map background"></div>
  <div class="abs footer-head" style="left:157px;top:3610px;width:110px">CITIES</div>
  <ul class="abs city-list">
    <li>Atlantic City</li><li>Bangkok</li><li>Beijing</li><li>Delhi</li><li>London</li><li>Los Angeles</li><li>New York</li>
  </ul>
  <div class="abs footer-head" style="left:523px;top:3610px;width:250px">ADVANCED SEARCH</div>
  <div class="abs field" style="left:355px;top:3670px;width:200px">Room / Flat</div>
  <div class="abs field" style="left:570px;top:3670px;width:200px">Enter the city</div>
  <div class="abs field" style="left:355px;top:3720px;width:110px">Min Price</div>
  <div class="abs field" style="left:478px;top:3720px;width:110px">Max Price</div>
  <div class="abs search-btn"></div>
  <div class="abs footer-head" style="left:710px;top:3805px;width:170px;font-size:19px">WE ARE SOCIAL</div>
  <div class="abs social-icon" style="left:935px;top:3800px;background:#c9302c"></div>
  <div class="abs social-icon" style="left:970px;top:3800px;background:#3b5a98"></div>
  <div class="abs social-icon" style="left:1005px;top:3800px;background:#2ea8dc"></div>
  <div class="abs social-icon" style="left:1040px;top:3800px;background:#9fb0c8"></div>
  <div class="abs legal-bar">
    <span class="abs" style="left:85px">Copyright © Flat Share. All Rights Reserved.</span>
    <span class="abs" style="left:940px">Privacy Policy</span>
    <span class="abs" style="left:1035px">Terms of Use</span>
  </div>
</footer>

</body>
</html>
```